Thistle Cafe's Web Page
Thank you for all the hardwork. Happy to see there are so many beautiful artworks. We have tried very hard to select the final winner. All the best in the year of Rabbit!!
We will post more contest later.Just stay tune!!
Good luck for all!!
good luck tremiko !!!
kindly rate template
thank you.
Can you kindly Rate our templates.
so that we will able to guess our work judgment.. how much effort we need more to create exact design!!!
Hi Guys! The reason I justified the work of Quillaro work is the outline of the web page not the software itself. When I look at the designs and the tones are mostly in black color and I think you will do the same thing as me. Do you all agree??
Corvel! your artwork is quite interesting too! Especially the slogan you made!! Your design is one of our consideration too!!
well i am waiting for your feedback. thanks
this whole thing is turning to a joke. enjoy
@ SirPlonk, Are you serious? You are only seeing part of my design. Please do not judge. Your comment is very offensive and you are belittling my work.
you're not serious are you ?
I think the design made by Quillarowork is quite attractive.
pomlet42 > Please let us know which designs you like so far. regards
Please check the design and rate :)
Best wishes
Wow! Quillarowork's design is quite nice. What's in the photo? Looks good!!
I found a website is quite interesting - http://www.brasvelo.com.au/. The designs that I recieved are similar. I hope the black color is not the only choice for us. Keep it going! Guys.Overall, the layouts are OK.
Just to verify, you will have both a set menu and a daily specials menu, is that correct. What other pages where you looking for on your site?
We are still renovating. It will be a good idea to spare some space for our cafe and our menu and special. We will be listen to any good suggestion!!
Logo has been uploaded
Thanks a lot :) I'M IN :)
Hi PH, Can you upload your logo so we know where to start? Thanks
We have a logo designed. It may be helpful to get some ideas. Please ask for it or browse the past projects (around late December) if needed.

```html
<!DOCTYPE html>
<html lang="en">
<head>
<meta charset="utf-8">
<title>Thistle Cafe</title>
<link rel="stylesheet" href="https://fonts.googleapis.com/css2?family=Open+Sans:wght@400;600;700&family=Lora:ital,wght@1,400;1,700&display=swap">
<style>
  :root{
    --orange:#c4420e;
    --orange-deep:#a7370a;
    --brown-dark:#2a120b;
    --brown-mid:#4a2214;
    --panel-line:#6b3a26;
    --text:#2b2b2b;
    --rule:#dcdcdc;
    --box-top:#f1f1f1;
    --white:#fff;
  }
  *{margin:0;padding:0;box-sizing:border-box}
  html,body{width:1200px;height:837px;overflow:hidden;background:var(--white)}
  body{position:relative;font-family:"Open Sans",Arial,sans-serif;color:var(--text)}

  .side-panel{position:absolute;left:12px;top:29px;width:372px;height:734px;
    background:linear-gradient(180deg,var(--brown-mid) 0%,var(--brown-dark) 60%,#1c0b06 100%);
    border:2px solid var(--panel-line);box-shadow:0 0 8px rgba(0,0,0,.35)}
  .brand{position:absolute;left:36px;top:50px;font-size:78px;font-weight:400;color:var(--orange);letter-spacing:1px;line-height:1}
  .tagline{position:absolute;left:44px;top:200px;font-family:"Lora",Georgia,serif;font-style:italic;font-size:29px;line-height:1.3;color:var(--white)}
  .side-photo{position:absolute;left:24px;top:326px;width:324px;height:396px;
    border:2px solid var(--panel-line);
    background:radial-gradient(ellipse at 50% 55%,#d9a274 0%,#8a4a26 35%,#3a1a0e 75%,#1d0c06 100%)}

  .main-nav{position:absolute;left:403px;top:62px;width:773px;display:flex;justify-content:space-between}
  .main-nav a{display:block;text-decoration:none;text-align:center;padding:0 6px;position:relative}
  .main-nav a + a::before{content:"";position:absolute;left:-18px;top:2px;height:42px;border-left:2px dotted #999}
  .main-nav .title{display:block;font-size:17px;font-weight:700;color:var(--orange);letter-spacing:.3px}
  .main-nav .sub{display:block;font-size:15px;color:var(--text);margin-top:6px}
  .main-nav a:first-child{text-align:left;padding-left:0}
  .main-nav a:last-child{text-align:right;padding-right:0}

  .content-box{position:absolute;left:403px;width:773px;background:var(--white);
    border:1px solid var(--rule);box-shadow:0 2px 6px rgba(0,0,0,.15)}
  .welcome{top:149px;height:295px}
  .box-head{height:70px;background:linear-gradient(180deg,var(--box-top),var(--white));padding:22px 24px 0}
  .welcome h1{font-size:36px;font-weight:400;color:var(--orange);letter-spacing:.2px;line-height:1.2}
  .welcome-copy{position:absolute;left:24px;top:84px;width:475px;font-size:14.5px;line-height:21px;color:var(--text)}
  .welcome-copy p + p{margin-top:14px}
  .read-more{position:absolute;left:350px;top:258px;font-size:15px;font-weight:700;color:var(--orange);text-decoration:none}
  .read-more span{text-decoration:underline}
  .welcome-photo{position:absolute;right:10px;top:84px;width:270px;height:185px;border-radius:50%;
    background:radial-gradient(ellipse at 50% 50%,#e0b07a 0%,#c46a2a 35%,#8a3f16 55%,rgba(255,255,255,0) 72%)}

  .specials{top:461px;height:307px}
  .specials h2{font-family:"Lora",Georgia,serif;font-style:italic;font-weight:700;font-size:31px;color:var(--orange);
    text-shadow:1px 1px 0 #5a1e05,2px 2px 3px rgba(0,0,0,.25)}
  .specials .box-head{padding-top:14px;height:62px}
  .special-list{position:absolute;left:50px;top:78px;width:430px;list-style:none}
  .special-list li{display:flex;justify-content:space-between;align-items:center;height:44px;font-size:15px;
    border-bottom:1px solid #eee;position:relative}
  .special-list li::before{content:"";position:absolute;left:-22px;top:19px;width:7px;height:7px;border-radius:50%;background:var(--orange)}
  .special-list .price{font-weight:700;color:var(--orange-deep)}
  .menu-board{position:absolute;right:22px;top:42px;width:170px;height:240px;
    background:linear-gradient(180deg,#7a3a16 0%,#a8582a 35%,#e9e4dc 36%,#f5f2ed 100%);border-radius:4px}

  .site-footer{position:absolute;left:0;top:787px;width:1200px;height:50px;background:var(--orange);
    color:var(--white);font-size:15px;text-align:center;line-height:50px}
</style>
</head>
<body>
  <aside class="side-panel">
    <div class="brand">Thistle</div>
    <p class="tagline">Make a pause...<br>and come to our house!</p>
    <div class="side-photo" role="img" aria-label="Plated grilled prawns and seafood dish"></div>
  </aside>

  <nav class="main-nav">
    <a href="#"><span class="title">ABOUT OUR CAFE</span><span class="sub">about us</span></a>
    <a href="#"><span class="title">MENU</span><span class="sub">what we offer</span></a>
    <a href="#"><span class="title">SPECIALS</span><span class="sub">special offers</span></a>
    <a href="#"><span class="title">RESERVATION</span><span class="sub">make reservation</span></a>
    <a href="#"><span class="title">CONTACTS</span><span class="sub">mailing address</span></a>
  </nav>

  <section class="content-box welcome">
    <div class="box-head"><h1>Welcome to Thistle Cafe!</h1></div>
    <div class="welcome-copy">
      <p>Our cafe is not focus on a large A-la Carte menu. We serve our food according to the weather, the freshest ingredients and the likeness of our customers. We put eastern ideas into western cuisine.</p>
      <p>We have 23 years of restaurant experience with passion in mastering our cuisine. We have a open kitchen and we use some raw materials such as brickworkand timber in our renovation.<br>An open decking area for outdoor dining.</p>
    </div>
    <a class="read-more" href="#">--&gt; <span>Read More</span></a>
    <div class="welcome-photo" role="img" aria-label="Grilled steak with vegetables on a plate"></div>
  </section>

  <section class="content-box specials">
    <div class="box-head"><h2>Specials in today's menu</h2></div>
    <ul class="special-list">
      <li><span>Sustryh hja kjtyu gtrte mter.</span><span class="price">$4.49</span></li>
      <li><span>Sustryh hja kjtyu gtrte mter.</span><span class="price">$6.49</span></li>
      <li><span>kurt jhd jksad yvwer aksdal.</span><span class="price">$4.38</span></li>
      <li><span>Sustryh hja kjtyu gtrte mter.</span><span class="price">$4.49</span></li>
      <li><span>Sustryh hja kjtyu gtrte mter.</span><span class="price">$4.49</span></li>
    </ul>
    <div class="menu-board" role="img" aria-label="Illustrated easel board reading Today's Menu with a chef"></div>
  </section>

  <footer class="site-footer">Copyright @ 2010 thistle cafe. All rights reserved. Privacy Policy</footer>
</body>
</html>
```